Plomberie DTR est une nouvelle entreprise de plomberie

Jaimerais maintenant des carte daffaire

Tendance
Avec un petit Puntch

Jaimerais quelque chose dans ce style avec le logo foncé plomberie dtr en facade
Jaimerais une photo en backgroung de fitting de plomberie comme je vous ai envoyer

Si vous voulez chercher une photo marquer sur google ( fitting norvak) pour vous donner des idee
Je veux que les fitting soit dune couleur pale en back ground pour faire ressortir mon logo

Toujours en facade de la carte je veux quil y ai mes services d'inscrit

Construction neuve
Reparation
Renovation
Urgence

514-286-5197
Rémi bouchardon

A larriere de la carte jaimerais le logo pâle plomberie DTR
Avec mes info
Email: info.dtrbatiment@exemple-courriel.ca
Rémi bouchardon
Cell: 514-286-5197
Plomberiedtr-exemple.ca

Voici des design que jai bien aimer libre a vous de vous laisser aller plus loin

Merci au plaisir de travailler avec vous

Target Market(s)

30 a 60 ans contracteur general

Industry/Entity Type

Construction plomberie

Contact Information for Business Card

Plomberie DTR inc. 514-286-5197 Rémi bouchardon. Plombier. info.dtrbatiment@exemple-courriel.ca

Font styles to use
Sans Serif

Colors
0054AA
0677BA
7BADD7
CADEEF
E8F1F8
F0912C
F2A743
F7CA91
FBE8D2
FDF5EE
EE7325
F08F49
F5BC92
FAE3D3
FDF4ED

Requirements
Must have
• Plombier serieux et virile jaime la couleur cuivre comme les fitting
Nice to have
• Carte transparente

```html
<!DOCTYPE html>
<html lang="fr">
<head>
<meta charset="utf-8">
<title>Plomberie DTR — cartes d'affaires</title>
<link href="https://fonts.googleapis.com/css2?family=Montserrat:wght@400;500;600;700&display=swap" rel="stylesheet">
<style>
  :root {
    --stage: #b9babd;
    --ink-dark: #141516;
    --photo-mid: #26282a;
    --copper: #c8713a;
    --copper-light: #e09650;
    --copper-deep: #93461f;
    --blue: #2f7fd0;
    --blue-dot: #3b8fe0;
    --paper: #f4f4f4;
    --grey-text: #4a4a4a;
    --white: #ffffff;
  }
  * { box-sizing: border-box; margin: 0; padding: 0; }
  html, body { width: 1200px; height: 960px; overflow: hidden; }
  body {
    background: var(--stage);
    font-family: "Montserrat", sans-serif;
    display: flex; flex-direction: column; align-items: center; justify-content: center; gap: 56px;
  }
  .card {
    position: relative; width: 700px; height: 400px; overflow: hidden;
    box-shadow: 0 6px 18px rgba(0,0,0,.25);
  }
  .photo-fill {
    position: absolute; inset: 0;
    background: radial-gradient(ellipse at 70% 65%, #34373a 0%, var(--photo-mid) 35%, var(--ink-dark) 80%);
  }
  .brand-name {
    position: absolute; color: var(--copper); font-weight: 700;
    text-transform: uppercase; letter-spacing: .18em; white-space: nowrap;
    display: flex; align-items: center; gap: 12px;
  }
  .brand-mark { width: 14px; height: 14px; background: var(--copper); }

  /* front */
  .card-front .brand-name { top: 150px; left: 0; right: 0; justify-content: center; font-size: 38px; }
  .services {
    position: absolute; left: 0; right: 0; top: 272px;
    display: flex; align-items: center; justify-content: center; gap: 14px;
    color: var(--white); font-size: 17px; font-weight: 500; letter-spacing: .04em;
  }
  .services li { list-style: none; display: flex; align-items: center; gap: 7px; }
  .services li::before { content: ""; width: 5px; height: 5px; border-radius: 50%; background: var(--blue-dot); }
  .pipe-cap { width: 38px; height: 18px; }

  /* back */
  .card-back { background: var(--paper); }
  .back-layout { position: absolute; inset: 0; }
  .card-back .brand-name { top: 62px; left: 60px; font-size: 30px; }
  .contact { position: absolute; left: 36px; top: 226px; }
  .contact-name { color: var(--blue); font-size: 27px; font-weight: 600; margin-bottom: 16px; }
  .contact-list { list-style: none; color: var(--grey-text); font-size: 17px; font-weight: 400; }
  .contact-list li { display: flex; align-items: center; gap: 10px; margin-bottom: 6px; }
  .contact-list svg { width: 16px; height: 16px; flex: none; fill: var(--blue); }
</style>
</head>
<body>

  <section class="card card-front" aria-label="Recto">
    <div class="photo-fill" role="img" aria-label="Photo sombre de raccords de plomberie en cuivre sertis"></div>
    <div class="brand-name"><span class="brand-mark"></span>Plomberie DTR</div>
    <ul class="services">
      <svg class="pipe-cap" viewBox="0 0 38 18"><rect x="0" y="4" width="28" height="10" fill="var(--copper)"/><rect x="28" y="0" width="6" height="18" fill="var(--copper-deep)"/></svg>
      <li>Construction neuve</li>
      <li>Reparation</li>
      <li>Renovation</li>
      <li>Urgence</li>
      <svg class="pipe-cap" viewBox="0 0 38 18"><rect x="4" y="0" width="6" height="18" fill="var(--copper-deep)"/><rect x="10" y="4" width="28" height="10" fill="var(--copper)"/></svg>
    </ul>
  </section>

  <section class="card card-back" aria-label="Verso">
    <svg class="back-layout" viewBox="0 0 700 400" aria-hidden="true">
      <defs>
        <linearGradient id="copperBand" x1="0" y1="0" x2="1" y2="0">
          <stop offset="0" stop-color="var(--copper-deep)"/>
          <stop offset=".5" stop-color="var(--copper-light)"/>
          <stop offset="1" stop-color="var(--copper-deep)"/>
        </linearGradient>
        <radialGradient id="photoTone" cx=".7" cy=".6" r=".8">
          <stop offset="0" stop-color="#34373a"/>
          <stop offset=".45" stop-color="#26282a"/>
          <stop offset="1" stop-color="#141516"/>
        </radialGradient>
      </defs>
      <polygon points="0,0 700,0 700,240 372,240 372,196 0,196" fill="url(#photoTone)" role="img" aria-label="Photo sombre de raccords de plomberie"/>
      <polyline points="0,200 366,200 366,246 700,246" fill="none" stroke="url(#copperBand)" stroke-width="12"/>
    </svg>
    <div class="brand-name"><span class="brand-mark"></span>Plomberie DTR</div>
    <div class="contact">
      <p class="contact-name">Rémi bouchardon</p>
      <ul class="contact-list">
        <li><svg viewBox="0 0 16 16"><path d="M3 1l3 3-2 2c1 2 3 4 5 5l2-2 3 3-2 3C6 14 2 10 1 3z"/></svg>514-286-5197</li>
        <li><svg viewBox="0 0 16 16"><path d="M1 3h14v10H1z M1 3l7 6 7-6" stroke="var(--paper)" stroke-width="1"/></svg>info.dtrbatiment@exemple-courriel.ca</li>
        <li><svg viewBox="0 0 16 16"><circle cx="8" cy="8" r="7"/><path d="M1 8h14M8 1c-3 4-3 10 0 14M8 1c3 4 3 10 0 14" stroke="var(--paper)" fill="none" stroke-width="1"/></svg>Plomberiedtr-exemple.ca</li>
      </ul>
    </div>
  </section>

</body>
</html>
```